Maple Hollow Pet Waste Alliance needs dog-centric 11"x17" flyer needed for a pet photo contest

We need a brochure for the Maple Hollow Pet Waste Alliance. They are holding a photo contest to encourage people to submit cute/funny photos of their dogs and sign a pledge to pick up pet waste.
The design should be eye catching and fun.
For a mockup, samples and specs, see the instructions attached or here:
https://slides.vexoranet.example/deck/7KdPqTzWmRbNcXyLfHgJvAsEoUiQe2Z8Ty4MnBwXcVbG/view?start=false&loop=false&delayms=3000

Target Market(s)

Dog owners in the Richmond Virginia metro area

Industry/Entity Type

Pet

Requirements
Must have
• Photo of dog (see samples in attached brief)
• Use the Maple Hollow Pet Waste Alliance Logo
• Have placeholders for sponsor listing
Nice to have
• Allusion to great prizes in flashy text

```html
<!DOCTYPE html>
<html lang="en">
<head>
<meta charset="utf-8">
<title>Pooches Against Poo Photo Contest</title>
<link rel="stylesheet" href="https://fonts.googleapis.com/css2?family=Archivo+Black&family=Arimo:wght@400;700&display=swap">
<style>
  :root {
    --orange: #f26a2e;
    --blue: #2a6fa3;
    --navy: #1f3f63;
    --ink: #222222;
    --paper-top: #ffffff;
    --paper-bottom: #e4e6e8;
  }
  * { margin: 0; padding: 0; box-sizing: border-box; }
  html, body { width: 778px; height: 1200px; overflow: hidden; }
  body {
    position: relative;
    background: linear-gradient(180deg, var(--paper-top) 0%, var(--paper-bottom) 100%);
    font-family: "Arimo", Arial, sans-serif;
    color: var(--ink);
  }
  .abs { position: absolute; }

  .hero-dog {
    left: 30px; top: 110px; width: 400px; height: 520px;
    background: linear-gradient(180deg, #e9e4dc 0%, #f6f3ee 60%, #dcd7cf 100%);
    border-radius: 45% 45% 16px 16px;
  }
  .title-top {
    left: 0; width: 778px; top: 18px;
    text-align: center;
    font-family: "Archivo Black", sans-serif;
    font-size: 62px; line-height: 1;
    color: var(--orange);
  }
  .title-poo {
    left: 0; width: 778px; top: 80px;
    text-align: center;
    font-family: "Archivo Black", sans-serif;
    font-size: 235px; line-height: 1; letter-spacing: 6px;
    color: var(--orange);
  }
  .subtitle {
    right: 30px; top: 336px;
    font-family: "Archivo Black", sans-serif;
    font-size: 46px; line-height: 1;
    color: var(--orange);
  }
  .tagline {
    right: 30px; top: 396px; width: 340px;
    text-align: right;
    font-weight: 700; font-size: 29px; line-height: 1.17;
  }
  .steps {
    left: 462px; top: 548px; width: 290px;
    list-style: none;
  }
  .steps li {
    position: relative;
    padding-left: 28px; margin-bottom: 10px;
    font-size: 16px; line-height: 1.2;
  }
  .steps li::before {
    content: ""; position: absolute; left: 4px; top: 3px;
    width: 13px; height: 13px; border-radius: 50%;
    background: var(--ink);
  }
  .win-badge {
    left: 256px; top: 528px; width: 172px; height: 172px;
    border-radius: 50%;
    background: var(--blue);
    border: 5px solid #ffffff;
    box-shadow: 0 2px 6px rgba(0,0,0,.25);
    color: #ffffff; text-align: center;
    display: flex; flex-direction: column; justify-content: center;
    font-family: "Archivo Black", sans-serif;
  }
  .win-badge .big { font-size: 38px; line-height: 1; }
  .win-badge .small { font-family: "Arimo", sans-serif; font-weight: 700; font-size: 18px; line-height: 1.1; margin-top: 2px; }
  .enter-label {
    left: 50px; top: 710px;
    font-weight: 700; font-size: 30px;
    color: var(--navy);
  }
  .enter-url {
    left: 0; width: 778px; top: 752px;
    text-align: center;
    font-weight: 700; font-size: 26px; letter-spacing: -0.6px;
    color: var(--blue);
  }
  .camera-dog {
    left: 40px; top: 805px; width: 160px; height: 180px;
    background: linear-gradient(180deg, #f1ede6 0%, #d9cfc0 100%);
    border-radius: 10px;
  }
  .deadline {
    left: 40px; top: 995px; width: 170px;
    font-size: 14px; line-height: 1.2;
  }
  .film-strip {
    left: 205px; top: 802px; width: 555px; height: 205px;
    background: linear-gradient(100deg, #2a2a2a 0%, #4a4a4a 50%, #2a2a2a 100%);
    border-radius: 8px;
    opacity: .9;
  }
  .alliance-mark {
    left: 462px; top: 1022px;
    display: flex; align-items: center; gap: 10px;
  }
  .alliance-mark .dot {
    width: 36px; height: 36px; border-radius: 50%;
    background: var(--ink);
  }
  .alliance-mark .name {
    font-weight: 700; font-size: 17px; line-height: 1.15;
    color: var(--navy); width: 240px;
  }
  .sponsored {
    left: 40px; top: 1090px;
    font-family: "Archivo Black", sans-serif;
    font-size: 40px;
    color: var(--orange);
  }
  .footer-band {
    left: 0; bottom: 0; width: 778px; height: 18px;
    background: var(--blue);
  }
</style>
</head>
<body>
  <div class="abs hero-dog" role="img" aria-label="Photo of a small terrier sitting cross-legged in a meditation pose"></div>

  <h1 class="abs title-top">Pooches Against</h1>
  <div class="abs title-poo">POO</div>

  <h2 class="abs subtitle">Photo Contest</h2>
  <p class="abs tagline">Achieve inner peace<br>with yourself,<br>your environment<br>and your dog!</p>

  <ul class="abs steps">
    <li>Enter the “Pooches Against Poo” photo contest today.</li>
    <li>Pledge to pick up pet waste and protect clean water.</li>
    <li>Ask your friends and family to vote for your adorable dog and win great prizes from our sponsors.</li>
  </ul>

  <div class="abs win-badge">
    <span class="big">WIN</span>
    <span class="big">GEAR</span>
    <span class="small">FOR YOUR<br>DOG</span>
  </div>

  <p class="abs enter-label">Enter today at:</p>
  <p class="abs enter-url">www.pawpage.example/MapleHollowPetWasteAlliance</p>

  <div class="abs camera-dog" role="img" aria-label="Photo of a dog wearing sunglasses holding a camera"></div>
  <p class="abs deadline">Submit your photo<br>by 06/12/2015</p>

  <div class="abs film-strip" role="img" aria-label="Film strip showing frames of dog photos entered in the contest"></div>

  <div class="abs alliance-mark">
    <span class="dot"></span>
    <span class="name">Maple Hollow Pet Waste Alliance</span>
  </div>

  <p class="abs sponsored">Sponsored by</p>

  <div class="abs footer-band"></div>
</body>
</html>
```